Anwaltskanzlei sucht Design für Geschäftspapier, Visitenkarten, Marketing unter Einbindung des neuen Logos
Zielgruppe
Anwaltliche Rechtsberatung und Rechtsvertretung auf den Gebieten des Arbeits-, Gesellschafts- und Wirtschaftsrechts sowie des Datenschutzrechts
Zielgruppe: Mittelständische Unternehmen aller Rechtsformen und Branchen
In Kooperation mit Kanzlei Velbrand (www.kanzlei-velbrand.de)
Inhaber einer weiteren Kanzlei Velbrand & Hossmer
Aufgabenstellung
Einbindung des übersandten Logos
ggf. Slogan: Kanzlei für den Mittelstand
optional: Nennung der Rechtsgebiete

```html
<!DOCTYPE html>
<html lang="de">
<head>
<meta charset="utf-8">
<title>Anwaltskanzlei Hossmer – Briefbogen</title>
<link rel="stylesheet" href="https://fonts.googleapis.com/css2?family=Montserrat:wght@300;400&family=Open+Sans:wght@400&display=swap">
<style>
  :root{
    --navy:#1f2e4d;
    --slate:#636985;
    --text-grey:#8a8a8a;
    --light-grey:#a3a3a3;
    --white:#ffffff;
  }
  *{margin:0;padding:0;box-sizing:border-box}
  html,body{width:848px;height:1200px;overflow:hidden;background:var(--white)}
  .letterhead{position:relative;width:848px;height:1200px;font-family:"Montserrat",sans-serif;color:var(--text-grey)}
  .header-stripe-top{position:absolute;left:0;top:0;width:848px;height:10px;background:var(--slate)}
  .header-band{position:absolute;left:0;top:10px;width:848px;height:73px;background:var(--navy)}
  .header-stripe-bottom{position:absolute;left:0;top:83px;width:848px;height:10px;background:var(--slate)}
  .brand-square{position:absolute;left:118px;top:44px;width:78px;height:74px;background:var(--navy);border:2px solid var(--white);border-radius:3px}
  .brand-name{position:absolute;left:628px;top:32px;width:112px;display:flex;align-items:center;gap:6px;color:var(--white);font-weight:400;font-size:9.6px;line-height:10.5px;letter-spacing:.2px;text-transform:uppercase}
  .brand-name .dot{width:7px;height:7px;background:var(--white);flex:none}
  .recipient-label{position:absolute;left:118px;top:236px;font-size:13.5px;color:var(--navy)}
  .recipient-name{position:absolute;left:118px;top:257px;font-size:14.6px;color:var(--navy)}
  .recipient-address{position:absolute;left:125px;top:280px;font-size:10.5px;font-weight:300;line-height:17.2px;color:var(--light-grey)}
  .letter-date{position:absolute;right:108px;top:238px;font-size:10.8px;color:var(--text-grey)}
  .letter-body{position:absolute;left:125px;top:382px;width:615px;font-size:13.9px;font-weight:300;line-height:17.1px;color:var(--text-grey);text-align:justify;hyphens:auto}
  .letter-body p{margin-bottom:17px}
  .signature{position:absolute;left:517px;top:909px;width:200px;height:92px;background:linear-gradient(90deg,rgba(31,46,77,.12),rgba(31,46,77,.22));border-radius:4px}
  .signer-role{position:absolute;right:108px;top:974px;font-size:16.4px;font-weight:300;color:var(--light-grey)}
  .footer-stripe{position:absolute;left:0;top:1130px;width:848px;height:11px;background:var(--slate)}
  .footer-band{position:absolute;left:0;top:1141px;width:848px;height:59px;background:var(--navy)}
  .contact{position:absolute;display:flex;align-items:center;gap:12px;color:var(--white);font-family:"Open Sans",sans-serif;font-size:9.8px;line-height:12.7px}
  .contact svg{flex:none}
  .contact-phone{left:157px;top:1158px}
  .contact-person{left:334px;top:1158px}
  .contact-address{left:559px;top:1150px}
</style>
</head>
<body>
<div class="letterhead">
  <div class="header-stripe-top"></div>
  <div class="header-band"></div>
  <div class="header-stripe-bottom"></div>
  <div class="brand-square"></div>
  <div class="brand-name"><span class="dot"></span><span>Anwaltskanzlei<br>Hossmer</span></div>

  <div class="recipient-label">TO</div>
  <div class="recipient-name">Name Surname</div>
  <div class="recipient-address">Human Resources<br>123 Inc.<br>1105-D ABCD, EFG<br>Germany</div>
  <div class="letter-date">Friday, 01/03/2022</div>

  <div class="letter-body" lang="la">
    <p>Lorem ipsum dolor sit amet, consectetur adipiscing elit. Pellentesque facilisis sollicitudin ante. Pellentesque habitant morbi tristique senectus et netus et malesuada fames ac turpis egestas. Nunc feugiat tortor nunc, quis feugiat lectus mattis sit amet. Nunc urna velit, convallis scelerisque odio non, pulvinar tincidunt massa. Proin pulvinar lacus at ex auctor consequat. Maecenas eleifend tempus posuere. Aliquam non pretium metus. Mauris nibh velit, molestie et lorem quis, hendrerit lacinia nunc. Donec in dignissim augue. Curabitur vitae erat nisi. Vestibulum ante ipsum primis in faucibus orci luctus et ultrices posuere cubilia Curae; Aliquam blandit magna ac augue placerat luctus. Ut et vehicula odio. Vivamus tincidunt diam diam, sed facilisis lectus pretium quis. Sed vel mi accumsan, luctus metus vel, congue ex.</p>
    <p>Curabitur non tristique tellus. Nam maximus fermentum metus sit amet luctus. Cras semper nunc id urna lacinia, in interdum quam mollis. Mauris sit amet eros vel lorem facilisis semper non ac nunc. Curabitur ornare suscipit lacus. Duis sit amet lectus vitae nulla consectetur ullamcorper vitae id urna. Sed dictum at lectus eget vehicula. Phasellus non lacinia nunc. Mauris ex tortor, ultricies luctus lectus egestas, gravida ornare elit. In tempor libero non ullamcorper sagittis. Phasellus interdum pulvinar lacus vel sodales. Praesent nec velit bibendum, accumsan magna non, molestie tortor. Nam a est at arcu porta auctor quis id tortor.</p>
    <p>Pellentesque habitant morbi tristique senectus et netus et malesuada fames ac turpis egestas. Nulla laoreet nec ex nec sagittis. Ut et vulputate magna. Nullam vehicula dapibus elit sagittis laoreet. Morbi dignissim ultricies libero at pulvinar. Sed leo tellus, ultricies nec erat sed, fermentum rhoncus odio. Pellentesque habitant morbi tristique senectus et netus et malesuada fames ac turpis egestas. Nullam egestas cursus dapibus. Nunc quis sodales nulla. Integer non ante tincidunt, facilisis mauris sed, rutrum neque.</p>
  </div>

  <div class="signature" role="img" aria-label="Handschriftliche Unterschrift des Absenders"></div>
  <div class="signer-role">Responsability</div>

  <div class="footer-stripe"></div>
  <div class="footer-band"></div>

  <div class="contact contact-phone">
    <svg width="23" height="23" viewBox="0 0 24 24" fill="none" stroke="#fff" stroke-width="1.3" stroke-linecap="round" stroke-linejoin="round"><path d="M5 2.5l3.5 4-2 2.5c1.5 3.2 4 5.8 7.3 7.3l2.5-2 4 3.5-2.3 3c-8 -.5 -15-7.5-15.5-15.5z"/><path d="M14 3.5a7 7 0 0 1 6.5 6.5"/><path d="M14 7a3.5 3.5 0 0 1 3 3"/></svg>
    <span>+49 (0) 30 55501928</span>
  </div>
  <div class="contact contact-person">
    <svg width="21" height="24" viewBox="0 0 21 24" fill="none" stroke="#fff" stroke-width="1.4"><circle cx="10.5" cy="6.5" r="5"/><path d="M1 23.5v-3a6.5 6.5 0 0 1 6.5-6.5h6a6.5 6.5 0 0 1 6.5 6.5v3"/></svg>
    <span>NAme Surname<br>N.Surname@kanzlei-hossmer.de</span>
  </div>
  <div class="contact contact-address">
    <svg width="20" height="24" viewBox="0 0 20 24" fill="none" stroke="#fff" stroke-width="1.4"><path d="M10 23s8.5-8.2 8.5-13.5a8.5 8.5 0 0 0-17 0C1.5 14.8 10 23 10 23z"/><circle cx="10" cy="9.5" r="3"/></svg>
    <span>123 Av.<br>4567 ABCD City<br>Germany</span>
  </div>
</div>
</body>
</html>
```